Storefront Sign Design for Rental Company

8ft x 8ft sign for the road in front of my business. I need something simple and clean but professional
Updates

Need extra days to review

Target Market(s)

Potential renters

Industry/Entity Type

Car Rental

Font styles to use
Serif
Sans Serif

Requirements
Must have
• Logo
• 832-555-0187
• DallasTrikeHire.example
• or
• www.DallasTrikeHire.example
• or
• DALLASTRIKEHIRE.EXAMPLE
• whichever looks better
Nice to have
• There is many cars that drive by each day so I would like something that shows my logo, phone number, and website

```html
<!DOCTYPE html>
<html lang="en">
<head>
<meta charset="utf-8">
<title>Dallas Trike Hire – Roadside Sign</title>
<link rel="stylesheet" href="https://fonts.googleapis.com/css2?family=Montserrat:wght@600;700;800&display=swap">
<style>
  :root {
    --backdrop: #e6e8eb;
    --sign-white: #ffffff;
    --ink: #1e1c1d;
    --stripe-mid: #575757;
    --stripe-dark: #2c2829;
    --photo-light: #cfcfcf;
    --photo-dark: #6a6a6a;
  }
  * { box-sizing: border-box; margin: 0; padding: 0; }
  html, body {
    width: 1200px;
    height: 900px;
    overflow: hidden;
    background: var(--backdrop);
  }
  .canvas {
    position: relative;
    width: 1200px;
    height: 900px;
  }
  .sign {
    position: absolute;
    left: 180px;
    top: 30px;
    width: 840px;
    height: 840px;
    background: var(--sign-white);
    overflow: hidden;
    box-shadow: 0 4px 18px rgba(0,0,0,0.12);
    font-family: "Montserrat", sans-serif;
    color: var(--ink);
  }
  .brand-name {
    position: absolute;
    top: 150px;
    left: 0;
    width: 100%;
    text-align: center;
    font-weight: 800;
    font-size: 46px;
    letter-spacing: 4px;
    text-transform: uppercase;
  }
  .phone-row {
    position: absolute;
    top: 252px;
    left: 0;
    width: 100%;
    display: flex;
    align-items: center;
    gap: 28px;
  }
  .phone-rule {
    flex: 1;
    height: 5px;
    background: var(--ink);
  }
  .phone {
    font-weight: 800;
    font-size: 68px;
    letter-spacing: 1px;
    line-height: 1;
  }
  .website {
    position: absolute;
    top: 350px;
    left: 0;
    width: 100%;
    text-align: center;
    font-weight: 700;
    font-size: 30px;
    letter-spacing: 3px;
  }
  .stripe {
    position: absolute;
    left: 0;
    width: 100%;
  }
  .stripe--mid { top: 470px; height: 80px; background: var(--stripe-mid); }
  .stripe--dark { top: 550px; height: 115px; background: var(--stripe-dark); }
  .vehicle-photo {
    position: absolute;
    left: 310px;
    top: 450px;
    width: 220px;
    height: 270px;
    background: linear-gradient(160deg, var(--photo-light), var(--photo-dark));
    border: 6px solid var(--sign-white);
  }
</style>
</head>
<body>
  <div class="canvas">
    <section class="sign">
      <h1 class="brand-name">Dallas Trike Hire</h1>
      <div class="phone-row">
        <span class="phone-rule"></span>
        <span class="phone">832-555-0187</span>
        <span class="phone-rule"></span>
      </div>
      <p class="website">www.DALLASTRIKEHIRE.example</p>
      <div class="stripe stripe--mid"></div>
      <div class="stripe stripe--dark"></div>
      <div class="vehicle-photo" role="img" aria-label="Black and white photo of a three-wheeled open roadster"></div>
    </section>
  </div>
</body>
</html>
```